Quorlan.com (Dedicated servers Provider)

We provide dedicated servers for clients around the world. We have created a layout for you. You need to create exactly the design based on these sketches. All text, you can take from our sketches (later we will replace them).

Target Market(s)

Web site owners and web developers

Requirements
Should not have
• The design should not use old-style fonts.

```html
<!DOCTYPE html>
<html lang="en">
<head>
<meta charset="utf-8">
<title>Quorlan Servers — Dedicated Servers Provider</title>
<link rel="stylesheet" href="https://fonts.googleapis.com/css2?family=Open+Sans:ital,wght@0,400;0,600;0,700;1,400;1,600&display=swap">
<style>
:root{
  --green:#7dbb2e;
  --green-dark:#5f9a1c;
  --ink:#2b2b2b;
  --nav:#3a3c40;
  --hero:#232323;
  --hero-side:#2e2e2e;
  --muted:#8a8a8a;
  --line:#dcdcdc;
  --price:#e0201b;
  --paper:#ffffff;
  --strip:#ececec;
  --footer:#1d1d1d;
  --footer-text:#9a9a9a;
}
*{box-sizing:border-box;margin:0;padding:0}
html,body{width:718px;height:1200px;overflow:hidden}
body{position:relative;background:var(--paper);font-family:"Open Sans",Arial,sans-serif;color:var(--ink);font-size:8px}
.abs{position:absolute}
a{color:inherit;text-decoration:none}

/* header */
.site-header{left:0;top:0;width:718px;height:56px;background:linear-gradient(#fff,#f1f1f1)}
.brand{left:57px;top:10px;display:flex;align-items:center;gap:6px}
.brand-mark{width:26px;height:26px;background:var(--ink)}
.brand-name{font-size:29px;font-weight:700;line-height:26px;color:var(--ink);letter-spacing:-0.5px}
.brand-sub{left:90px;top:36px;font-size:8px;color:var(--green);letter-spacing:2px}
.help-icon{left:438px;top:4px;width:16px;height:16px;border-radius:50%;background:#111;color:#fff;font-weight:700;font-size:12px;text-align:center;line-height:16px}
.call-label{left:456px;top:11px;font-size:9px;font-weight:700}
.call-phone{left:568px;top:5px;font-size:15px;font-weight:700;color:var(--green)}
.top-btn{top:34px;height:14px;padding:0 7px;border-radius:7px;background:var(--ink);color:#fff;font-size:6.5px;font-weight:600;line-height:14px;white-space:nowrap}

/* nav */
.main-nav{left:0;top:56px;width:718px;height:22px;background:linear-gradient(#4a4c51,#2f3135)}
.nav-home{left:57px;top:0;width:31px;height:22px;background:var(--green)}
.nav-item{top:0;line-height:22px;color:#fff;font-size:7px}
.nav-order{left:551px;top:0;width:94px;height:22px;background:var(--green);color:#fff;font-weight:700;font-size:9px;text-align:center;line-height:22px}
.announce{left:0;top:78px;width:718px;height:14px;background:var(--green);color:#fff;font-size:6.5px;line-height:14px}
.social-dot{top:80px;width:11px;height:11px;border-radius:2px;background:#fff}

/* hero */
.hero{left:0;top:92px;width:718px;height:186px;background:var(--hero)}
.hero-side{left:410px;top:92px;width:235px;height:186px;background:var(--hero-side)}
.hero-servers{left:72px;top:100px;width:180px;height:172px;background:linear-gradient(180deg,#3a3a3a,#111);border-radius:4px}
.hero-title{left:187px;top:112px;font-size:21px;font-weight:700;color:#fff;letter-spacing:-0.3px}
.hero-from{left:330px;top:138px;font-size:7px;font-style:italic;color:#fff;font-weight:600}
.hero-list{left:263px;top:161px;list-style:none;color:#fff;font-size:7.5px}
.hero-list li{height:15px;padding-left:10px;position:relative}
.hero-list li::before{content:"»";position:absolute;left:0;color:#aaa}
.btn-green{background:var(--green);color:#fff;font-weight:600;text-align:center;border:1px solid var(--green-dark)}
.hero-cta{left:273px;top:242px;width:75px;height:16px;font-size:7px;line-height:14px}
.hero-quote{left:426px;top:126px;width:140px;font-style:italic;color:#ddd;font-size:10px;line-height:17px}
.hero-quote-src{left:492px;top:179px;font-size:7px;color:#aaa}
.hero-person{left:485px;top:95px;width:160px;height:183px;background:linear-gradient(160deg,#6a6a6a,#c9c9c9 60%,#8a8a8a)}

/* hiring strip */
.hiring{left:0;top:278px;width:718px;height:42px;background:linear-gradient(#f3f3f3,#e2e2e2)}
.hiring-label{left:93px;top:284px;font-size:8px;font-weight:700}
.hiring-btn{left:93px;top:297px;width:57px;height:10px;font-size:5px;line-height:8px}
.sales{left:443px;top:289px;font-size:12px;font-weight:600;color:var(--ink)}

/* plans */
.tabs{left:57px;top:338px;width:588px;height:22px;background:#2d2d2d}
.tab{top:338px;height:22px;line-height:22px;color:#fff;font-size:7.5px;font-weight:600;text-align:center}
.tab.is-active{background:var(--green)}
.plans{left:57px;top:360px;width:588px;height:248px;border:1px solid var(--line);border-top:0;background:linear-gradient(#fff,#f9f9f9)}
.plan-divider{top:372px;width:1px;height:128px;background:var(--line)}
.plan-title{top:378px;font-size:11px;font-weight:600;width:195px;text-align:center}
.plan-art{top:398px;width:86px;height:34px;background:linear-gradient(90deg,#b9b9b9,#e4e4e4,#a0a0a0);border-radius:2px}
.plan-from{font-size:5px;color:#555;width:50px;text-align:right}
.plan-price{font-size:21px;font-weight:700;color:var(--price);letter-spacing:-1px}
.plan-price sup{font-size:10px;vertical-align:9px}
.plan-specs{font-size:5.5px;line-height:8px;color:#333}
.plan-select{width:70px;height:9px;border:1px solid #bbb;border-radius:2px;font-size:5px;line-height:7px;padding-left:4px;background:#fff}
.plan-link{font-size:5.5px;text-decoration:underline}
.plan-order{width:30px;height:10px;font-size:6px;line-height:8px}
.plans-rule{left:57px;top:510px;width:588px;height:1px;background:var(--line)}
.coverage-map{left:80px;top:520px;width:110px;height:72px;background:radial-gradient(ellipse at 55% 50%,#8ed041,#c8c8c8 70%,transparent 72%)}
.coverage-note{left:88px;top:597px;font-size:5.5px;color:#444}
.feature{font-size:8px;display:flex;align-items:center;gap:8px}
.tick{width:12px;height:12px;border-radius:50%;background:var(--green);display:flex;align-items:center;justify-content:center}

/* testimonial */
.arrow{top:662px;font-size:22px;color:#777;font-weight:400}
.testi-photo{left:100px;top:638px;width:90px;height:68px;border:3px solid #fff;box-shadow:0 0 0 1px #ddd,0 2px 3px rgba(0,0,0,.15);background:linear-gradient(#dadada,#9a9a9a)}
.testi-quote{left:205px;top:646px;width:410px;font-style:italic;color:#999;font-size:9px;line-height:12.5px}
.testi-name{left:202px;top:688px;font-size:7px;color:#888}
.testi-site{left:202px;top:698px;font-size:6px;color:#aaa}

/* partner strip */
.partners{left:0;top:732px;width:718px;height:50px;background:var(--strip);border-top:1px solid #e0e0e0}
.partner{top:750px;height:14px;background:#b8b8b8;border-radius:2px}

/* footer */
.footer{left:0;top:782px;width:718px;height:418px;background:var(--footer)}
.f-title{font-size:10px;font-weight:600;color:#fff}
.f-title em{font-style:normal;color:var(--green)}
.f-feature-icon{width:24px;height:24px}
.f-feature-title{font-size:6.5px;font-weight:700;color:#fff}
.f-feature-text{font-size:5.5px;color:var(--footer-text);line-height:8px;width:115px}
.f-rule{left:62px;width:583px;height:1px;background:#333}
.stat-dot{width:9px;height:9px;border-radius:50%;background:#fff}
.stat-num{font-size:17px;color:#fff;font-weight:400}
.stat-text{font-size:5px;color:var(--footer-text);line-height:7px;width:80px}
.f-col-title{font-size:9px;font-weight:600;color:var(--green)}
.f-col-text{font-size:6.5px;color:#fff;line-height:10px}
.f-phone{left:474px;top:1092px;font-size:16px;font-weight:600;color:#fff}
.f-social{top:1119px;width:14px;height:14px;border-radius:50%}
.f-more{left:63px;top:1123px;font-size:6px;color:var(--green);font-weight:600}
.f-logo{top:1166px;height:14px;background:#e8e8e8;border-radius:2px}
.award{left:474px;top:1163px;font-size:5.5px;font-weight:700;color:#fff;line-height:7px}
.award small{color:var(--green);font-size:4.5px;font-weight:400;display:block}
.award-badge{left:540px;top:1162px;width:34px;height:20px;border-radius:50%;background:#bbb}
.sitemap{left:590px;top:1168px;width:48px;height:11px;background:#3a3a3a;color:#fff;font-size:5px;text-align:center;line-height:11px;border:1px solid #555}
</style>
</head>
<body>

<header class="site-header abs"></header>
<div class="brand abs"><span class="brand-mark"></span><span class="brand-name">Quorlan</span></div>
<div class="brand-sub abs">servers</div>
<div class="help-icon abs">?</div>
<div class="call-label abs">Questions? Call Now!</div>
<div class="call-phone abs">0.800.000.QRLN</div>
<a class="top-btn abs" style="left:408px">USER REGISTRATION</a>
<a class="top-btn abs" style="left:488px">CUSTOMER LOGIN</a>
<a class="top-btn abs" style="left:572px">LIVE CHAT ONLINE</a>

<nav class="main-nav abs">
  <a class="nav-home abs" aria-label="Home"><svg width="31" height="22" viewBox="0 0 31 22"><path d="M9 11l6.5-6 6.5 6h-2v6h-3v-4h-3v4h-3v-6z" fill="#fff"/></svg></a>
  <a class="nav-item abs" style="left:111px">Domains</a>
  <a class="nav-item abs" style="left:183px">Web Hosting</a>
  <a class="nav-item abs" style="left:274px">Latest News</a>
  <a class="nav-item abs" style="left:365px">My Account</a>
  <a class="nav-item abs" style="left:456px">Contact Us</a>
  <a class="nav-order abs">ORDER NOW!</a>
</nav>
<div class="announce abs">
  <span class="abs" style="left:100px">▭&nbsp; Got an important announcement or a special offer? Tell your customer about it! <b style="color:#2b2b2b;font-weight:400">Read More</b></span>
  <span class="abs" style="left:557px;font-weight:600">Follow Us</span>
</div>
<span class="social-dot abs" style="left:596px"></span>
<span class="social-dot abs" style="left:612px"></span>
<span class="social-dot abs" style="left:628px"></span>

<section class="hero abs"></section>
<div class="hero-side abs"></div>
<div class="hero-servers abs" role="img" aria-label="Three dark server tower cabinets"></div>
<h1 class="hero-title abs">DEDICATED SERVERS</h1>
<div class="hero-from abs">FROM QUORLAN</div>
<ul class="hero-list abs">
  <li>Self-owned data centre</li>
  <li>24 x 7 x 365 on-site support</li>
  <li>100% uptime guarantee</li>
  <li>Industry leading control panel</li>
  <li>Custom servers; 24 hour setup</li>
</ul>
<a class="hero-cta btn-green abs">FIND OUT MORE</a>
<div class="hero-person abs" role="img" aria-label="Smiling customer in a grey suit"></div>
<p class="hero-quote abs">“Glad I managed to choose one of the few companies with good customer service”</p>
<div class="hero-quote-src abs">brightlane.example</div>

<section class="hiring abs"></section>
<svg class="abs" style="left:62px;top:283px" width="24" height="28" viewBox="0 0 24 28"><circle cx="12" cy="7" r="6" fill="#111"/><path d="M1 27c0-8 5-12 11-12s11 4 11 12z" fill="#111"/></svg>
<div class="hiring-label abs">WE ARE HIRING</div>
<a class="hiring-btn btn-green abs">APPLY ONLINE NOW</a>
<div class="sales abs">CALL SALES TODAY <b>01632 960 418</b></div>

<div class="tabs abs"></div>
<a class="tab is-active abs" style="left:57px;width:122px">Dedicated Servers</a>
<a class="tab abs" style="left:179px;width:111px">Web Hosting</a>
<a class="tab abs" style="left:290px;width:140px">Virtual Private Server</a>
<section class="plans abs"></section>
<span class="plan-divider abs" style="left:250px"></span>
<span class="plan-divider abs" style="left:445px"></span>

<h2 class="plan-title abs" style="left:43px">Vireo 4 2.4 GHz</h2>
<div class="plan-art abs" style="left:100px" role="img" aria-label="Processor and server unit"></div>
<div class="plan-from abs" style="left:84px;top:445px">Plans starting at</div>
<div class="plan-price abs" style="left:83px;top:450px">$39<sup>00</sup></div>
<div class="plan-from abs" style="left:84px;top:465px">per mo.</div>
<div class="plan-specs abs" style="left:146px;top:443px">80GB SATA HD<br>1GB RAM<br>1TB Bandwidth</div>
<div class="plan-select abs" style="left:146px;top:467px">1 year – 39.00/mo ▾</div>
<a class="plan-link abs" style="left:79px;top:485px">All Dedicated Servers</a>
<a class="plan-order btn-green abs" style="left:148px;top:483px">ORDER</a>

<h2 class="plan-title abs" style="left:243px">Corvex i7 2.66-2.93 GHz</h2>
<div class="plan-art abs" style="left:297px" role="img" aria-label="Processor and server unit"></div>
<div class="plan-from abs" style="left:279px;top:445px">Plans starting at</div>
<div class="plan-price abs" style="left:277px;top:450px">$219<sup>00</sup></div>
<div class="plan-from abs" style="left:279px;top:465px">per mo.</div>
<div class="plan-specs abs" style="left:350px;top:443px">500GB SATA HD<br>6GB RAM<br>8TB Bandwidth</div>
<div class="plan-select abs" style="left:350px;top:467px">1 year – 39.00/mo ▾</div>
<a class="plan-link abs" style="left:287px;top:485px">All Dedicated Servers</a>
<a class="plan-order btn-green abs" style="left:354px;top:483px">ORDER</a>

<h2 class="plan-title abs" style="left:435px">Dual Zenith E5-2620</h2>
<div class="plan-art abs" style="left:489px" role="img" aria-label="Processor and server unit"></div>
<div class="plan-from abs" style="left:471px;top:445px">Plans starting at</div>
<div class="plan-price abs" style="left:469px;top:450px">$395<sup>00</sup></div>
<div class="plan-from abs" style="left:471px;top:465px">per mo.</div>
<div class="plan-specs abs" style="left:543px;top:443px">1000GB SATA HD<br>16GB RAM<br>10TB Bandwidth</div>
<div class="plan-select abs" style="left:543px;top:467px">1 year – 39.00/mo ▾</div>
<a class="plan-link abs" style="left:477px;top:485px">All Dedicated Servers</a>
<a class="plan-order btn-green abs" style="left:546px;top:483px">ORDER</a>

<span class="plans-rule abs"></span>
<div class="coverage-map abs" role="img" aria-label="Map of the network with green coast-to-coast links"></div>
<div class="coverage-note abs">Now Offering Nimbus Host Panel 11</div>
<div class="feature abs" style="left:255px;top:529px"><span class="tick"><svg width="8" height="8" viewBox="0 0 8 8"><path d="M1 4l2 2 4-4" stroke="#fff" stroke-width="1.6" fill="none"/></svg></span>100% Network Uptime SLA</div>
<div class="feature abs" style="left:255px;top:553px"><span class="tick"><svg width="8" height="8" viewBox="0 0 8 8"><path d="M1 4l2 2 4-4" stroke="#fff" stroke-width="1.6" fill="none"/></svg></span>ISO 9001:2008 Certified</div>
<div class="feature abs" style="left:255px;top:577px"><span class="tick"><svg width="8" height="8" viewBox="0 0 8 8"><path d="M1 4l2 2 4-4" stroke="#fff" stroke-width="1.6" fill="none"/></svg></span>24/7 ITIL Technical Support</div>
<div class="feature abs" style="left:428px;top:529px"><span class="tick"><svg width="8" height="8" viewBox="0 0 8 8"><path d="M1 4l2 2 4-4" stroke="#fff" stroke-width="1.6" fill="none"/></svg></span>3 SSAE-16 Certified Data Centers</div>
<div class="feature abs" style="left:428px;top:553px"><span class="tick"><svg width="8" height="8" viewBox="0 0 8 8"><path d="M1 4l2 2 4-4" stroke="#fff" stroke-width="1.6" fill="none"/></svg></span>Coast-to-Coast IP Backbone</div>
<div class="feature abs" style="left:428px;top:577px"><span class="tick"><svg width="8" height="8" viewBox="0 0 8 8"><path d="M1 4l2 2 4-4" stroke="#fff" stroke-width="1.6" fill="none"/></svg></span>Award Winning Since 1996</div>

<span class="arrow abs" style="left:66px">‹</span>
<span class="arrow abs" style="left:620px">›</span>
<div class="testi-photo abs" role="img" aria-label="Portrait of the company CEO"></div>
<p class="testi-quote abs"><span style="font-size:20px;color:#ccc;line-height:8px">“</span>Lorem Ipsum is simply dummy text of the printing and typesetting industry. Lorem Ipsum has been the industry's standard dummy text ever since the 1500s, Lorem Ipsum is simply dummy text of the printing and typesetting industry. <span style="font-size:20px;color:#ccc;line-height:8px">”</span></p>
<div class="testi-name abs">Daniel Marsh | C.E.O.</div>
<div class="testi-site abs">marshstudio.example</div>

<section class="partners abs"></section>
<span class="partner abs" style="left:80px;width:26px;border-radius:50%"></span>
<span class="partner abs" style="left:128px;width:14px;height:18px;top:748px"></span>
<span class="partner abs" style="left:163px;width:34px"></span>
<span class="partner abs" style="left:218px;width:38px"></span>
<span class="partner abs" style="left:273px;width:34px"></span>
<span class="partner abs" style="left:330px;width:24px;height:18px;top:748px"></span>
<span class="partner abs" style="left:376px;width:32px"></span>
<span class="partner abs" style="left:422px;width:36px;height:8px;top:753px"></span>
<span class="partner abs" style="left:477px;width:28px"></span>
<span class="partner abs" style="left:523px;width:34px"></span>
<span class="partner abs" style="left:578px;width:38px"></span>

<footer class="footer abs"></footer>
<h3 class="f-title abs" style="left:62px;top:803px"><em>Quorlan Servers - </em>&nbsp;Dedicated servers Provider</h3>

<svg class="f-feature-icon abs" style="left:79px;top:833px" viewBox="0 0 24 24"><rect x="2" y="3" width="20" height="6" rx="1" fill="#fff"/><rect x="2" y="11" width="20" height="6" rx="1" fill="#fff"/><rect x="4" y="20" width="16" height="2" fill="#fff"/></svg>
<div class="f-feature-title abs" style="left:112px;top:832px">Lorem Ipsum is simply dummy text</div>
<div class="f-feature-text abs" style="left:112px;top:842px">Lorem Ipsum is simply dummy text of the printing and typesetting industry.</div>
<svg class="f-feature-icon abs" style="left:281px;top:832px" viewBox="0 0 24 24"><circle cx="12" cy="12" r="10" fill="none" stroke="#fff" stroke-width="2"/><ellipse cx="12" cy="12" rx="4" ry="10" fill="none" stroke="#fff" stroke-width="1.5"/><path d="M2 12h20M4 7h16M4 17h16" stroke="#fff" stroke-width="1.5"/></svg>
<div class="f-feature-title abs" style="left:315px;top:832px">Lorem Ipsum is simply dummy text</div>
<div class="f-feature-text abs" style="left:315px;top:842px">Lorem Ipsum is simply dummy text of the printing and typesetting industry.</div>
<svg class="f-feature-icon abs" style="left:479px;top:832px" viewBox="0 0 24 24"><rect x="3" y="15" width="18" height="6" rx="1" fill="#fff"/><path d="M12 15V8" stroke="#fff" stroke-width="2"/><path d="M7 7a7 7 0 0 1 10 0M9 9.5a4 4 0 0 1 6 0" stroke="#fff" stroke-width="1.5" fill="none"/></svg>
<div class="f-feature-title abs" style="left:513px;top:832px">Lorem Ipsum is simply dummy text</div>
<div class="f-feature-text abs" style="left:513px;top:842px">Lorem Ipsum is simply dummy text of the printing and typesetting industry.</div>

<svg class="f-feature-icon abs" style="left:79px;top:884px" viewBox="0 0 24 24"><rect x="8" y="1" width="8" height="6" fill="#fff"/><path d="M12 7v4M4 11h16M4 11v4M12 11v4M20 11v4" stroke="#fff" stroke-width="1.5"/><rect x="1" y="15" width="6" height="6" fill="#fff"/><rect x="9" y="15" width="6" height="6" fill="#fff"/><rect x="17" y="15" width="6" height="6" fill="#fff"/></svg>
<div class="f-feature-title abs" style="left:112px;top:882px">Lorem Ipsum is simply dummy text</div>
<div class="f-feature-text abs" style="left:112px;top:892px">Lorem Ipsum is simply dummy text of the printing and typesetting industry.</div>
<svg class="f-feature-icon abs" style="left:281px;top:884px" viewBox="0 0 24 24"><circle cx="15" cy="9" r="5" fill="none" stroke="#fff" stroke-width="3" stroke-dasharray="2.5 1.5"/><circle cx="7" cy="17" r="4" fill="none" stroke="#fff" stroke-width="3" stroke-dasharray="2 1.3"/></svg>
<div class="f-feature-title abs" style="left:315px;top:882px">Lorem Ipsum is simply dummy text</div>
<div class="f-feature-text abs" style="left:315px;top:892px">Lorem Ipsum is simply dummy text of the printing and typesetting industry.</div>
<svg class="f-feature-icon abs" style="left:479px;top:884px" viewBox="0 0 24 24"><rect x="3" y="2" width="18" height="6" rx="1" fill="#fff"/><rect x="3" y="9" width="18" height="6" rx="1" fill="#fff"/><rect x="3" y="16" width="18" height="6" rx="1" fill="#fff"/></svg>
<div class="f-feature-title abs" style="left:513px;top:882px">Lorem Ipsum is simply dummy text</div>
<div class="f-feature-text abs" style="left:513px;top:892px">Lorem Ipsum is simply dummy text of the printing and typesetting industry.</div>

<span class="f-rule abs" style="top:930px"></span>
<h3 class="f-title abs" style="left:62px;top:947px"><em>Quorlan Servers - </em>&nbsp;check out our stats!</h3>
<span class="stat-dot abs" style="left:72px;top:973px"></span>
<div class="stat-num abs" style="left:89px;top:966px">2,500,000</div>
<div class="stat-text abs" style="left:89px;top:990px">Domains registered in over 250 extensions</div>
<span class="stat-dot abs" style="left:235px;top:973px"></span>
<div class="stat-num abs" style="left:253px;top:966px">50,000</div>
<div class="stat-text abs" style="left:253px;top:990px">new registrations per month</div>
<span class="stat-dot abs" style="left:375px;top:973px"></span>
<div class="stat-num abs" style="left:393px;top:966px">800,000</div>
<div class="stat-text abs" style="left:393px;top:990px">new registrations per month</div>
<span class="stat-dot abs" style="left:517px;top:973px"></span>
<div class="stat-num abs" style="left:534px;top:966px">1,000,000</div>
<div class="stat-text abs" style="left:534px;top:990px">clients are using our products</div>

<span class="f-rule abs" style="top:1027px"></span>
<h4 class="f-col-title abs" style="left:62px;top:1045px">Lorem Ipsum is simply dummy text</h4>
<p class="f-col-text abs" style="left:62px;top:1062px;width:175px">Lorem Ipsum is simply dummy text of the printing and typesetting industry. Lorem Ipsum has been the industry's standard dummy text ever since the 1500s, when an unknown printer took a galley of type and scrambled it to make a type specimen book.</p>
<a class="f-more abs">Learn more about it.</a>

<h4 class="f-col-title abs" style="left:309px;top:1045px">About Quorlan Servers</h4>
<p class="f-col-text abs" style="left:309px;top:1062px">About Us<br>Domains<br>Web Hosting</p>
<p class="f-col-text abs" style="left:365px;top:1062px">Latest News<br>My Account<br>Contact Us</p>
<p class="f-col-text abs" style="left:309px;top:1097px">Copyright © Quorlan Servers Ltd 2012.<br>All rights reserved</p>

<h4 class="f-col-title abs" style="left:473px;top:1045px">Information</h4>
<p class="f-col-text abs" style="left:474px;top:1062px;width:175px">Contact us via our Support Ticket System in your Online Control Panel or alternatively call us on the number below:</p>
<div class="f-phone abs">01632 960 418</div>
<span class="f-social abs" style="left:475px;background:#3b6fb6"></span>
<span class="f-social abs" style="left:496px;background:#3fa9e0"></span>
<span class="f-social abs" style="left:517px;background:#e8742a"></span>

<span class="f-rule abs" style="top:1147px"></span>
<span class="f-logo abs" style="left:64px;width:20px;border-radius:50%;height:20px;top:1163px"></span>
<span class="f-logo abs" style="left:92px;width:40px"></span>
<span class="f-logo abs" style="left:141px;width:40px"></span>
<span class="f-logo abs" style="left:191px;width:40px"></span>
<span class="f-logo abs" style="left:240px;width:12px;height:12px;top:1167px"></span>
<span class="f-logo abs" style="left:260px;width:42px"></span>
<span class="f-logo abs" style="left:312px;width:26px;border-radius:50%;height:18px;top:1164px"></span>
<div class="award abs">AWARD WINNING<br>DEDICATED HOSTING<small>View Our Awards</small></div>
<span class="award-badge abs"></span>
<a class="sitemap abs">SHOW SITEMAP</a>

</body>
</html>
```